Größen anpassen für versch. Werbemittel
Zielgruppe
Wir organisieren Messen rund um die Frau!
Aufgabenstellung
Das Layout steht soweit und müsste nur angepasst werden.
Wir benötigen folgendes:
Das beigefügte Plakat in folgenden Größen:
a1 - sollen bei Papierfalke gedruclt werden!
a3 - II
2m² Traffic Bord 120x75 ohne Beschnitt-Hochformat-Schriften vektorisieren!
Berliner Rahmen: Plakatdruck 2/1-(A0)-Querformat 84,1 x 118,5 cm, 115 g Affichenpapier 4-farbirg Euroskala
Großflächen: S. Anlage
LED Tafeln:
Immer der Fotocredit Brigitte Solweck dazu! Wichtig!
Das Logo aber sollte oben hin, dann das Foto, darunter der Text.
Irgendwo sollte noch dazu:
Die Trend- und Eventmesse rund um die Frau (oder ähnlich),
damit man direkt weiß, um was es geht ;)

```html
<!DOCTYPE html>
<html lang="de">
<head>
<meta charset="utf-8">
<title>LUMEA – Trend- &amp; Eventmesse – Formate</title>
<link rel="stylesheet" href="https://fonts.googleapis.com/css2?family=Open+Sans:wght@300;400;700&display=swap">
<style>
  :root {
    --magenta: #c8186a;
    --ink: #1e1e1e;
    --grey: #4a4a4a;
    --white: #ffffff;
    --stage: #e8e8ea;
  }
  * { margin: 0; padding: 0; box-sizing: border-box; }
  html, body { width: 1200px; height: 849px; overflow: hidden; background: var(--stage); }
  .formats { position: relative; width: 1200px; height: 849px; }

  .poster {
    position: absolute;
    display: flex;
    flex-direction: column;
    background: var(--white);
    font-family: "Open Sans", Arial, sans-serif;
    box-shadow: 0 2px 8px rgba(0,0,0,0.18);
    overflow: hidden;
  }
  .poster--portrait  { left: 24px;  top: 24px;  width: 566px; height: 801px; font-size: 5.66px; }
  .poster--landscape { left: 614px; top: 24px;  width: 562px; height: 399px; font-size: 2.8px; }
  .poster--traffic   { left: 777px; top: 447px; width: 236px; height: 378px; font-size: 2.36px; }

  .brand {
    flex: 0 0 15%;
    display: flex;
    align-items: center;
    justify-content: center;
    font-weight: 300;
    font-size: 16em;
    letter-spacing: 0.3em;
    padding-left: 0.3em;
    color: var(--ink);
    line-height: 1;
  }
  .poster--landscape .brand { flex-basis: 17%; }

  .divider {
    flex: 0 0 1.2%;
    background: var(--magenta);
    box-shadow: 0 0.5em 0.7em rgba(0,0,0,0.25);
    position: relative;
    z-index: 1;
  }

  .hero-photo {
    position: relative;
    flex: 0 0 36%;
    background:
      linear-gradient(90deg, rgba(120,120,118,0.75) 0%, rgba(200,203,201,0.2) 28%, rgba(0,0,0,0) 45%),
      linear-gradient(100deg, #9a9a96 0%, #cfd2d0 22%, #a87a58 38%, #c99c7c 52%, #eadfd8 68%, #f3f1ee 100%);
  }
  .poster--landscape .hero-photo { flex-basis: 38%; }
  .photo-credit {
    position: absolute;
    left: 2.2em;
    bottom: 1.6em;
    font-size: 1.5em;
    color: var(--ink);
  }

  .info {
    flex: 1 1 auto;
    display: flex;
    flex-direction: column;
    justify-content: center;
    gap: 1.8em;
    text-align: center;
  }
  .headline {
    color: var(--magenta);
    font-weight: 700;
    font-size: 6.4em;
    line-height: 1.15;
  }
  .event-details {
    color: var(--grey);
    font-weight: 700;
    font-size: 5em;
    line-height: 1.2;
  }
  .claim {
    color: var(--magenta);
    font-weight: 400;
    font-size: 3.8em;
    line-height: 1.25;
  }
  .info-side { display: flex; flex-direction: column; gap: 2.4em; }

  .poster--landscape .info {
    flex-direction: row;
    align-items: center;
    justify-content: space-around;
    gap: 0;
  }

  .footer-band {
    flex: 0 0 9%;
    display: flex;
    align-items: center;
    justify-content: center;
    background: var(--magenta);
    color: var(--white);
    font-weight: 700;
    font-size: 7em;
  }
  .poster--landscape .footer-band { flex-basis: 11%; }
</style>
</head>
<body>
  <main class="formats">

    <article class="poster poster--portrait">
      <header class="brand">LUMEA</header>
      <div class="divider"></div>
      <div class="hero-photo" role="img" aria-label="Porträtfoto einer lächelnden Frau mit schulterlangem braunem Haar vor hellem Hintergrund">
        <p class="photo-credit">Fotocredit: Brigitte Solweck</p>
      </div>
      <section class="info">
        <h1 class="headline">TREND -<br>&amp; EVENTMESSE<br>rund um die Frau</h1>
        <p class="event-details">29 &amp; 30 April 2017<br>Kongresshaus Velden</p>
        <p class="claim">DEIN TAG ZUM WOHLFÜHLEN,<br>SCHÖNSEIN, LAUTLACHEN,<br>SACHENMACHEN</p>
      </section>
      <footer class="footer-band">www.lumea-messen.de</footer>
    </article>

    <article class="poster poster--landscape">
      <header class="brand">LUMEA</header>
      <div class="divider"></div>
      <div class="hero-photo" role="img" aria-label="Porträtfoto einer lächelnden Frau mit schulterlangem braunem Haar vor hellem Hintergrund">
        <p class="photo-credit">Fotocredit: Brigitte Solweck</p>
      </div>
      <section class="info">
        <h1 class="headline">TREND -<br>&amp; EVENTMESSE<br>rund um die Frau</h1>
        <div class="info-side">
          <p class="event-details">29 &amp; 30 April 2017<br>Kongresshaus Velden</p>
          <p class="claim">DEIN TAG ZUM WOHLFÜHLEN,<br>SCHÖNSEIN, LAUTLACHEN,<br>SACHENMACHEN</p>
        </div>
      </section>
      <footer class="footer-band">www.lumea-messen.de</footer>
    </article>

    <article class="poster poster--traffic">
      <header class="brand">LUMEA</header>
      <div class="divider"></div>
      <div class="hero-photo" role="img" aria-label="Porträtfoto einer lächelnden Frau mit schulterlangem braunem Haar vor hellem Hintergrund">
        <p class="photo-credit">Fotocredit: Brigitte Solweck</p>
      </div>
      <section class="info">
        <h1 class="headline">TREND -<br>&amp; EVENTMESSE<br>rund um die Frau</h1>
        <p class="event-details">29 &amp; 30 April 2017<br>Kongresshaus Velden</p>
        <p class="claim">DEIN TAG ZUM WOHLFÜHLEN,<br>SCHÖNSEIN, LAUTLACHEN,<br>SACHENMACHEN</p>
      </section>
      <footer class="footer-band">www.lumea-messen.de</footer>
    </article>

  </main>
</body>
</html>
```